Business card for Luxury Portable Restroom Trailer company

We are a Luxury Portable Restroom Trailer Company Called PELIKAR HIRES. Based in Orange County California. We provide portable restroom trailers for events, such as, Weddings, Concerts, Charity events, Sporting events, Tournaments, Corporate events, ect. We rent and Sell the Luxury restrooms. Our colors are white, grey, and Orange. As you will see in the logo we uploaded.
There are 2 people in the company so the names and titles will change for the 3 people but card will remain the same. Here is the information for each Person: Dennis Moyle CFO 555 018-3647
next Person: Wesley Tanford VP 555 018-3647
Next Person: Miles Tanford CEO 555 018-3647
Information to include on the card: Luxury Restroom Trailers Rental and Sales. Weddings, Concerts, Charity, Sporting and Corp. Events.

```html
<!DOCTYPE html>
<html lang="en">
<head>
<meta charset="utf-8">
<title>PELIKAR HIRES – Business Card</title>
<link href="https://fonts.googleapis.com/css2?family=Source+Sans+3:ital,wght@0,400;0,600;0,700;1,400;1,600&display=swap" rel="stylesheet">
<style>
  :root {
    --orange: #f26f2d;
    --grey: #58585a;
    --line: #8a8a8a;
    --paper: #ffffff;
    --page: #ffffff;
  }
  * { box-sizing: border-box; margin: 0; padding: 0; }
  html, body { width: 1200px; height: 991px; overflow: hidden; background: var(--page); }
  body { position: relative; font-family: "Source Sans 3", sans-serif; color: var(--grey); }

  .card {
    position: absolute;
    left: 302px;
    width: 600px;
    height: 343px;
    background: var(--paper);
    border: 1px solid var(--line);
    overflow: hidden;
  }
  .card--front { top: 113px; }
  .card--back { top: 544px; }

  /* Front */
  .wordmark {
    position: absolute;
    left: 0; right: 0; top: 48px;
    text-align: center;
    font-size: 44px;
    font-weight: 700;
    letter-spacing: 1px;
    color: var(--orange);
  }
  .hero-art {
    position: absolute;
    left: 0; top: 142px;
    width: 300px; height: 201px;
    background: radial-gradient(ellipse at 30% 60%, rgba(242,111,45,0.22), rgba(242,111,45,0.04) 70%, rgba(242,111,45,0) 100%);
  }
  .person {
    position: absolute;
    left: 330px; width: 160px; top: 211px;
    text-align: center;
  }
  .person__name { font-size: 26px; font-weight: 600; font-style: italic; line-height: 30px; white-space: nowrap; margin-left: -40px; margin-right: -40px; }
  .person__title, .person__phone { font-size: 22px; line-height: 28px; }

  /* Back */
  .back-lines { position: absolute; inset: 0; }
  .tagline {
    position: absolute;
    left: 334px; top: 35px;
    font-size: 18px; font-style: italic; line-height: 23px;
  }
  .tagline__dots { color: var(--orange); font-weight: 700; font-style: normal; letter-spacing: 1px; }
  .company {
    position: absolute;
    left: 14px; width: 200px; top: 279px;
    text-align: center; font-size: 18px; line-height: 21px;
  }
  .event-list { list-style: none; }
  .event-list__item { position: absolute; height: 22px; right: 35px; }
  .event-list__item svg { position: absolute; inset: 0; width: 100%; height: 100%; overflow: visible; }
  .event-list__label {
    position: absolute; inset: 0;
    text-align: center; font-size: 17px; line-height: 22px; padding-left: 10px;
  }
</style>
</head>
<body>

<section class="card card--front" aria-label="Business card front">
  <div class="wordmark">PELIKAR HIRES</div>
  <div class="hero-art" role="img" aria-label="Large orange line decoration of the brand animal"></div>
  <div class="person">
    <div class="person__name">Miles Tanford</div>
    <div class="person__title">CEO</div>
    <div class="person__phone">555 018-3647</div>
  </div>
</section>

<section class="card card--back" aria-label="Business card back">
  <svg class="back-lines" viewBox="0 0 600 343" width="600" height="343">
    <g fill="none" stroke="var(--orange)">
      <circle cx="105.6" cy="85.8" r="167" stroke-width="17"/>
      <path d="M296.4 0 A210 210 0 0 1 206.4 270" stroke-width="1.6"/>
      <path d="M349.2 115.8 A246 246 0 0 1 0 308" stroke-width="1.6"/>
      <circle cx="105.6" cy="85.8" r="510" stroke-width="1.6"/>
    </g>
    <text x="150" y="104" text-anchor="middle" font-family="Source Sans 3, sans-serif" font-size="22" font-weight="700" fill="var(--orange)">PELIKAR HIRES</text>
  </svg>

  <p class="tagline">We provide portable Luxury<br>Restroom Trailers Rental &amp; Sales<br>for <span class="tagline__dots">....</span></p>

  <ul class="event-list">
    <li class="event-list__item" style="left:390px;top:118px;">
      <svg viewBox="0 0 175 22" preserveAspectRatio="none"><path d="M2 0 H164 A11 11 0 0 1 164 22 H0 Z" fill="none" stroke="var(--orange)" stroke-width="1.3"/></svg>
      <span class="event-list__label">Weddings</span>
    </li>
    <li class="event-list__item" style="left:382px;top:149px;">
      <svg viewBox="0 0 183 22" preserveAspectRatio="none"><path d="M5 0 H172 A11 11 0 0 1 172 22 H0 Z" fill="none" stroke="var(--orange)" stroke-width="1.3"/></svg>
      <span class="event-list__label">Concerts</span>
    </li>
    <li class="event-list__item" style="left:370px;top:180px;">
      <svg viewBox="0 0 195 22" preserveAspectRatio="none"><path d="M8 0 H184 A11 11 0 0 1 184 22 H0 Z" fill="none" stroke="var(--orange)" stroke-width="1.3"/></svg>
      <span class="event-list__label">Charity</span>
    </li>
    <li class="event-list__item" style="left:355px;top:211px;">
      <svg viewBox="0 0 210 22" preserveAspectRatio="none"><path d="M12 0 H199 A11 11 0 0 1 199 22 H0 Z" fill="none" stroke="var(--orange)" stroke-width="1.3"/></svg>
      <span class="event-list__label">Sporting</span>
    </li>
    <li class="event-list__item" style="left:333px;top:242px;">
      <svg viewBox="0 0 232 22" preserveAspectRatio="none"><path d="M15 0 H221 A11 11 0 0 1 221 22 H0 Z" fill="none" stroke="var(--orange)" stroke-width="1.3"/></svg>
      <span class="event-list__label">Tournaments</span>
    </li>
    <li class="event-list__item" style="left:304px;top:273px;">
      <svg viewBox="0 0 261 22" preserveAspectRatio="none"><path d="M19 0 H250 A11 11 0 0 1 250 22 H0 Z" fill="none" stroke="var(--orange)" stroke-width="1.3"/></svg>
      <span class="event-list__label">Corporate Events</span>
    </li>
  </ul>

  <div class="company">
    <div>PELIKAR HIRES</div>
    <div>555 018-3647</div>
  </div>
</section>

</body>
</html>
```